Atendimento nota 11, sem contar a agilidade das pessoas, nos apresentaram diversos modelos e formas de logo. Com certeza iremos indica-lo para outras pessoas.

```html
<!DOCTYPE html>
<html lang="pt-BR">
<head>
<meta charset="UTF-8">
<title>Lumen Imóveis – Bloco de notas</title>
<link rel="stylesheet" href="https://fonts.googleapis.com/css2?family=Raleway:wght@300;400;500&display=swap">
<style>
  :root {
    --bg: #ebebeb;
    --brown: #3b2a1f;
    --brown-soft: #463328;
    --gold: #c8a66e;
    --paper: #ffffff;
    --rule: #8c8c8c;
    --coil: #9a9a9a;
    --ink: #3b2a1f;
  }
  * { margin: 0; padding: 0; box-sizing: border-box; }
  html, body { width: 1200px; height: 1200px; overflow: hidden; }
  body {
    background: var(--bg);
    position: relative;
    font-family: "Raleway", sans-serif;
  }
  .notepad {
    position: absolute;
    box-shadow: 0 6px 14px rgba(0,0,0,0.18);
  }
  .notepad--cover, .notepad--back {
    background: var(--brown);
    top: 420px; width: 278px; height: 396px;
  }
  .notepad--cover { left: 161px; }
  .notepad--back { left: 763px; }
  .notepad--sheet {
    background: var(--paper);
    left: 468px; top: 384px; width: 276px; height: 401px;
  }
  .coil {
    position: absolute; top: -10px; left: 14px; right: 14px; height: 26px;
  }
  .gold-rule {
    position: absolute; left: 0; right: 0; bottom: 22px;
    height: 2px; background: var(--gold);
  }
  .brand {
    position: absolute; left: 0; right: 0; top: 148px;
    text-align: center; color: var(--gold);
  }
  .brand__mark {
    width: 30px; height: 30px; background: var(--gold);
    margin: 0 auto 14px;
  }
  .brand__name {
    font-weight: 400; font-size: 38px; letter-spacing: 1px; line-height: 1;
  }
  .brand__tag {
    font-weight: 400; font-size: 13px; letter-spacing: 7px; margin-top: 6px;
  }
  .ruled-lines {
    position: absolute; left: 38px; right: 38px; top: 54px; height: 240px;
    background: repeating-linear-gradient(to bottom,
      transparent 0, transparent 9px, var(--rule) 9px, var(--rule) 10px);
  }
  .sheet-brand {
    position: absolute; left: 0; right: 0; bottom: 24px;
    text-align: center; color: var(--ink);
    font-weight: 500; font-size: 14px; letter-spacing: 2px;
  }
  .back-backdrop {
    position: absolute; left: 0; top: 50px; width: 278px; height: 300px;
    background: linear-gradient(135deg, var(--brown-soft), var(--brown));
  }
  .back-brand {
    position: absolute; left: 0; right: 0; top: 296px;
    text-align: center; color: var(--gold);
    font-weight: 500; font-size: 16px; letter-spacing: 2px;
  }
  .back-address {
    position: absolute; left: 0; right: 0; top: 340px;
    text-align: center; color: #e8dccb;
    font-size: 9px; line-height: 1.5; font-weight: 400;
  }
</style>
</head>
<body>
  <svg width="0" height="0" style="position:absolute">
    <defs>
      <pattern id="coil-loop" width="12.5" height="26" patternUnits="userSpaceOnUse">
        <ellipse cx="6" cy="13" rx="4" ry="7" fill="none" stroke="#9a9a9a" stroke-width="1.6"/>
      </pattern>
    </defs>
  </svg>

  <section class="notepad notepad--cover">
    <svg class="coil" viewBox="0 0 250 26" preserveAspectRatio="none"><rect width="250" height="26" fill="url(#coil-loop)"/></svg>
    <div class="brand">
      <div class="brand__mark"></div>
      <div class="brand__name">LUMEN</div>
      <div class="brand__tag">IMÓVEIS</div>
    </div>
    <div class="gold-rule"></div>
  </section>

  <section class="notepad notepad--sheet">
    <svg class="coil" viewBox="0 0 248 26" preserveAspectRatio="none"><rect width="248" height="26" fill="url(#coil-loop)"/></svg>
    <div class="ruled-lines"></div>
    <div class="sheet-brand">LUMEN</div>
  </section>

  <section class="notepad notepad--back">
    <div class="back-backdrop"></div>
    <svg class="coil" viewBox="0 0 250 26" preserveAspectRatio="none"><rect width="250" height="26" fill="url(#coil-loop)"/></svg>
    <div class="back-brand">LUMEN</div>
    <p class="back-address">Rua das Acácias, nº 45, Sala 03, Centro - Vila Mar - SC<br>CEP: 00000-000 - (00) 0000-0000</p>
    <div class="gold-rule"></div>
  </section>
</body>
</html>
```